Infographics for Zenfolk

Zenfolk company specializes in providing services for the organization of low-budget crowdsourcing research.
Crowdsourcing research - the solution of the problem by lots of people on a competitive basis. Types of research will not be limited to the design competition, and will cover all areas of economic activity.

The site contains the following sections: directory of research, user communities, where they can organize the communication according to common interests, forum, news ticker.

The site will feature two groups of users:
1. Organizers of commercial research - the firm or individual businessmen
2. Researchers of commercial research. Moreover, the organizers can act as executors in the research organized by other users.

Motives Organizers of research:
1. Solving business problems quickly and inexpensively, and the variability of solutions.
2. The possibility of recruiting the best researchers.
3. Self-promotion (positioning your company as an innovative, using cutting-edge technology solutions).
4. Doing Business with the times.

The motives of researchers:
1. Earnings with their knowledge by participating in competitions and receive the prize fund.
2. Employability organized research (if the customer makes an offer the researcher).
3. Intelligent Leisure
4. Communication: forum, chat with the professionals of their field of study.

Required:
Graphically show the behavior of two groups of people based on their motives.
Schematically, the sheet should be divided into two parts - the left diagram of the model of the organizers, to the right - the researchers. The middle - it is desirable that part where the researchers will provide solutions to problems of the organizers - the scheme intersect each other graphically.
This work will be used for placement on the website of the company, as well as in printed promotional products.

Target Market(s)

Entrepreneurs, businesses as well as economically active population of Russia

Industry/Entity Type

Communication

Requirements
Must have
• The company's logo from the attached file.
All decals made with cursive. All decails are editable.
The source file in vector format EPS.
Nice to have
• The color scheme of the site will match the logo, so it is desirable that the figure used the same color as the logo: black, gray, green. In an attachment, "firm color" color settings in the CMYK.
Schemes must come from the top down, page orientation - portrait.
Should not have
• Do not use photos. Only pictures.

```html
<!DOCTYPE html>
<html lang="en">
<head>
<meta charset="utf-8">
<title>Zenfolk — Organizers and Researchers</title>
<link rel="stylesheet" href="https://fonts.googleapis.com/css2?family=Bebas+Neue&family=Quicksand:wght@400&display=swap">
<style>
  :root {
    --yellow: #ffd800;
    --amber: #ffc20e;
    --cream: #fdf8d2;
    --charcoal: #3b3d3f;
    --green: #8dc63f;
    --green-deep: #6fa82b;
    --white: #ffffff;
  }
  * { margin: 0; padding: 0; box-sizing: border-box; }
  html, body { width: 900px; height: 1200px; overflow: hidden; }
  body { background: var(--cream); font-family: "Bebas Neue", "Arial Narrow", sans-serif; }
  .sheet { position: relative; width: 900px; height: 1200px; overflow: hidden; background: var(--cream); }
  .header {
    position: absolute; left: 0; top: 0; width: 900px; height: 130px;
    background: linear-gradient(105deg, var(--yellow) 0 48%, var(--amber) 48% 100%);
  }
  .brand {
    position: absolute; left: 70px; top: 28px;
    font-family: "Quicksand", sans-serif; font-weight: 400; font-size: 64px;
    color: var(--charcoal); letter-spacing: 1px; line-height: 1;
    display: flex; align-items: center; gap: 14px;
  }
  .brand-dot { width: 22px; height: 22px; border-radius: 50%; background: var(--green); }
  .footer { position: absolute; left: 0; bottom: 0; width: 900px; height: 25px; background: var(--yellow); }
  .panels { position: absolute; left: 0; top: 0; }
  .label { position: absolute; line-height: 0.92; white-space: nowrap; }
  .label.right { text-align: right; }
  .g { color: var(--green); }
  .w { color: var(--white); }
  .d { color: var(--charcoal); }
  .column-title { position: absolute; font-size: 64px; line-height: 1; top: 172px; }
  .icon { position: absolute; border-radius: 14px; }
  .icon.on-dark { background: rgba(141, 198, 63, 0.35); }
  .icon.on-green { background: rgba(59, 61, 63, 0.28); }
</style>
</head>
<body>
<main class="sheet">
  <header class="header">
    <div class="brand"><span class="brand-dot"></span>Zenfolk</div>
  </header>

  <svg class="panels" width="900" height="1200" viewBox="0 0 900 1200">
    <!-- column headings -->
    <polygon fill="var(--charcoal)" points="0,162 470,162 428,204 470,246 0,246"/>
    <polygon fill="var(--green)" points="490,162 900,162 900,246 490,246 446,204"/>
    <!-- motive rows -->
    <g fill="var(--charcoal)">
      <polygon points="58,300 470,300 400,394 470,488 58,488"/>
      <polygon points="58,510 470,510 400,604 470,698 58,698"/>
      <polygon points="58,720 470,720 400,814 470,908 58,908"/>
      <polygon points="58,930 470,930 400,1024 470,1118 58,1118"/>
    </g>
    <g fill="var(--green)">
      <polygon points="497,300 840,300 840,488 497,488 430,394"/>
      <polygon points="497,510 840,510 840,698 497,698 430,604"/>
      <polygon points="497,720 840,720 840,908 497,908 430,814"/>
      <polygon points="497,930 840,930 840,1118 497,1118 430,1024"/>
    </g>
  </svg>

  <div class="column-title g" style="left:86px;">Organizers</div>
  <div class="column-title d" style="left:533px;">Researchers</div>

  <!-- Row 1 -->
  <div class="label" style="left:84px; top:322px;">
    <div style="font-size:25px;"><span class="g">Solve</span> <span class="w">Business</span></div>
    <div class="g" style="font-size:38px;">Problems</div>
    <div class="w" style="font-size:38px;">Quickly</div>
    <div class="g" style="font-size:27px;">And</div>
    <div class="w" style="font-size:27px;">Inexpensively</div>
  </div>
  <div class="icon on-dark" role="img" aria-label="Light bulb with a dollar sign" style="left:283px; top:328px; width:88px; height:134px;"></div>
  <div class="icon on-green" role="img" aria-label="Number one award ribbon" style="left:506px; top:333px; width:90px; height:118px;"></div>
  <div class="label right" style="right:72px; top:340px; font-size:38px;">
    <div class="d">Received</div>
    <div><span class="w">The</span> <span class="d">Prize</span> <span class="w">Fund</span></div>
    <div><span class="d">In</span><span class="w">Competitions</span></div>
  </div>

  <!-- Row 2 -->
  <div class="label" style="left:80px; top:538px;">
    <div class="g" style="font-size:54px;">Recruit</div>
    <div style="font-size:54px;"><span class="w">The</span><span class="g">Best</span></div>
    <div class="w" style="font-size:31px;">Researchers</div>
  </div>
  <div class="icon on-dark" role="img" aria-label="Group of people with one highlighted" style="left:262px; top:564px; width:126px; height:78px;"></div>
  <div class="icon on-green" role="img" aria-label="People talking and two connected computers" style="left:552px; top:534px; width:90px; height:146px;"></div>
  <div class="label" style="left:645px; top:564px; font-size:42px;">
    <div class="w">Intelligent</div>
    <div class="d">Leisure</div>
  </div>

  <!-- Row 3 -->
  <div class="label" style="left:80px; top:772px;">
    <div class="g" style="font-size:54px;">Self</div>
    <div class="w" style="font-size:31px;">Promotion</div>
  </div>
  <div class="icon on-dark" role="img" aria-label="Web page with a chart and a computer mouse" style="left:232px; top:740px; width:134px; height:150px;"></div>
  <div class="icon on-green" role="img" aria-label="Two computers exchanging messages" style="left:500px; top:738px; width:100px; height:150px;"></div>
  <div class="label" style="left:600px; top:780px;">
    <div class="w" style="font-size:38px;">Communication</div>
    <div style="font-size:28px;"><span class="d">With</span> <span class="w">Professionals</span></div>
  </div>

  <!-- Row 4 -->
  <div class="label" style="left:80px; top:985px;">
    <div class="g" style="font-size:50px;">Do</div>
    <div class="w" style="font-size:31px;">Business</div>
  </div>
  <div class="icon on-dark" role="img" aria-label="Stack of banknotes" style="left:218px; top:964px; width:154px; height:118px;"></div>
  <div class="icon on-green" role="img" aria-label="Handshake" style="left:490px; top:990px; width:100px; height:70px;"></div>
  <div class="label" style="left:598px; top:1002px; font-size:52px;">
    <span class="d">Employ</span><span class="w">ment</span>
  </div>

  <footer class="footer"></footer>
</main>
</body>
</html>
```